8 x 8 - Social Media Posting - Bright Key DPA Program

Buyer(s) Need Down Payment Assistance?
OUR BRIGHTKEY PROGRAM
offers all you need....
* Grant Up to 3.5% of Purchase Price
* No Down Payment (FHA Only)
* 600 Minimum Score
* No Max DTI Requirement (As Determined by AUS)
* No First Time Home Buyer Requirement
* No Minimum Borrower Contribution
* Non Occupant Co-Borrowers Allowed
Call us today at (800) 417-2960
Harborlane Lending Services, Inc.
7200 Wexmoor Road, Brentmoor, MD 21099
www.harborlanelend.example
NMLS #318674

```html
<!DOCTYPE html>
<html lang="en">
<head>
<meta charset="utf-8">
<title>Bright Key DPA Program</title>
<link rel="stylesheet" href="https://fonts.googleapis.com/css2?family=Montserrat:wght@600;700&family=Lato:wght@400;700&display=swap">
<style>
  :root {
    --navy-light: #2a4ba0;
    --navy: #1b3783;
    --navy-dark: #122a68;
    --gold: #d9a94a;
    --gold-light: #f0cf7a;
    --red: #d81b4c;
    --red-dark: #b4103c;
    --paper: #ffffff;
    --paper-grey: #e9eaee;
    --ink: #1f2c5c;
    --ink-soft: #4a5068;
  }
  * { margin: 0; padding: 0; box-sizing: border-box; }
  html, body { width: 1200px; height: 1200px; overflow: hidden; }
  body { position: relative; background: var(--paper); font-family: "Lato", sans-serif; }
  .backdrop { position: absolute; inset: 0; width: 1200px; height: 1200px; }
  .headline {
    position: absolute; left: 646px; top: 98px;
    font-family: "Montserrat", sans-serif; font-weight: 700;
    font-size: 54px; line-height: 70px; color: var(--paper); letter-spacing: 0.3px;
  }
  .program {
    position: absolute; left: 646px; top: 342px;
    font-family: "Montserrat", sans-serif; font-weight: 600;
    color: var(--paper); font-size: 28px; line-height: 42px; letter-spacing: 0.8px;
  }
  .program .tail { font-size: 29px; letter-spacing: 0.4px; }
  .benefits { position: absolute; left: 644px; top: 490px; list-style: none; }
  .benefits li {
    position: relative; height: 100px; padding-left: 78px;
    color: var(--paper); font-size: 28px; line-height: 34px;
  }
  .benefits svg { position: absolute; left: 0; top: 4px; width: 36px; height: 36px; }
  .cta {
    position: absolute; left: 48px; top: 582px; width: 534px; height: 210px;
    border-radius: 14px; background: linear-gradient(180deg, var(--red), var(--red-dark));
    box-shadow: 0 8px 18px rgba(0,0,0,0.25);
    color: var(--paper); text-align: center;
  }
  .cta-label { margin-top: 48px; font-family: "Montserrat", sans-serif; font-weight: 600; font-size: 25px; letter-spacing: 0.5px; }
  .cta-phone { margin-top: 14px; font-family: "Montserrat", sans-serif; font-weight: 700; font-size: 50px; letter-spacing: 0.5px; }
  .brand {
    position: absolute; left: 94px; top: 894px;
    display: flex; align-items: center; gap: 12px;
    font-family: "Montserrat", sans-serif; font-weight: 700; font-size: 24px; color: var(--ink);
  }
  .brand-dot { width: 22px; height: 22px; border-radius: 50%; background: var(--gold); }
  .company { position: absolute; left: 90px; top: 1000px; color: var(--ink-soft); font-size: 23px; line-height: 30px; font-style: normal; }
  .company .name, .company .web { color: var(--ink); font-weight: 700; }
</style>
</head>
<body>
  <svg class="backdrop" viewBox="0 0 1200 1200" aria-hidden="true">
    <defs>
      <linearGradient id="navyFill" x1="0" y1="0" x2="1" y2="1">
        <stop offset="0" stop-color="var(--navy-light)"/>
        <stop offset="0.55" stop-color="var(--navy)"/>
        <stop offset="1" stop-color="var(--navy-dark)"/>
      </linearGradient>
      <linearGradient id="paperFill" x1="0" y1="0" x2="0" y2="1">
        <stop offset="0" stop-color="var(--paper-grey)"/>
        <stop offset="1" stop-color="var(--paper)"/>
      </linearGradient>
      <linearGradient id="goldFill" x1="0" y1="0" x2="0" y2="1">
        <stop offset="0" stop-color="var(--gold)"/>
        <stop offset="0.5" stop-color="var(--gold-light)"/>
        <stop offset="1" stop-color="var(--gold)"/>
      </linearGradient>
      <linearGradient id="photoFill" x1="0" y1="0" x2="1" y2="1">
        <stop offset="0" stop-color="#b88a6a"/>
        <stop offset="0.5" stop-color="#7a5a48"/>
        <stop offset="1" stop-color="#5d6f8c"/>
      </linearGradient>
    </defs>
    <rect x="0" y="740" width="600" height="460" fill="url(#paperFill)"/>
    <polygon points="498,0 1200,0 1200,1200 492,1200 564,948 498,740 600,348" fill="url(#navyFill)"/>
    <polygon points="462,0 498,0 600,348 498,740 462,740 566,348" fill="url(#goldFill)"/>
  </svg>
  <svg class="backdrop" viewBox="0 0 1200 1200" role="img" aria-label="Photo of a smiling couple holding house keys in front of a brick home with a sold sign">
    <polygon points="0,0 462,0 566,348 462,740 0,740" fill="url(#photoFill)"/>
  </svg>

  <h1 class="headline">BUYER(S) NEED<br>DOWN PAYMENT<br>ASSISTANCE?</h1>

  <p class="program">OUR BRIGHTKEY PROGRAM<br><span class="tail">offers all you need....</span></p>

  <ul class="benefits">
    <li><svg viewBox="0 0 36 36"><circle cx="18" cy="18" r="17" fill="var(--gold)"/><path d="M10 18.5l5.5 5.5L26.5 12" fill="none" stroke="var(--navy)" stroke-width="3.6" stroke-linecap="round" stroke-linejoin="round"/></svg>Grant Up to 3.5% of<br>Purchase Price</li>
    <li><svg viewBox="0 0 36 36"><circle cx="18" cy="18" r="17" fill="var(--gold)"/><path d="M10 18.5l5.5 5.5L26.5 12" fill="none" stroke="var(--navy)" stroke-width="3.6" stroke-linecap="round" stroke-linejoin="round"/></svg>No Down Payment<br>(FHA Only)</li>
    <li><svg viewBox="0 0 36 36"><circle cx="18" cy="18" r="17" fill="var(--gold)"/><path d="M10 18.5l5.5 5.5L26.5 12" fill="none" stroke="var(--navy)" stroke-width="3.6" stroke-linecap="round" stroke-linejoin="round"/></svg>600 Minimum Score</li>
    <li><svg viewBox="0 0 36 36"><circle cx="18" cy="18" r="17" fill="var(--gold)"/><path d="M10 18.5l5.5 5.5L26.5 12" fill="none" stroke="var(--navy)" stroke-width="3.6" stroke-linecap="round" stroke-linejoin="round"/></svg>No Max DTI Requirement<br>(As Determined by AUS)</li>
    <li><svg viewBox="0 0 36 36"><circle cx="18" cy="18" r="17" fill="var(--gold)"/><path d="M10 18.5l5.5 5.5L26.5 12" fill="none" stroke="var(--navy)" stroke-width="3.6" stroke-linecap="round" stroke-linejoin="round"/></svg>No First Time Home Buyer<br>Requirement</li>
    <li><svg viewBox="0 0 36 36"><circle cx="18" cy="18" r="17" fill="var(--gold)"/><path d="M10 18.5l5.5 5.5L26.5 12" fill="none" stroke="var(--navy)" stroke-width="3.6" stroke-linecap="round" stroke-linejoin="round"/></svg>No Minimum Borrower<br>Contribution</li>
    <li><svg viewBox="0 0 36 36"><circle cx="18" cy="18" r="17" fill="var(--gold)"/><path d="M10 18.5l5.5 5.5L26.5 12" fill="none" stroke="var(--navy)" stroke-width="3.6" stroke-linecap="round" stroke-linejoin="round"/></svg>Non Occupant<br>Co-Borrowers Allowed</li>
  </ul>

  <div class="cta">
    <p class="cta-label">CALL US TODAY!</p>
    <p class="cta-phone">(800) 417-2960</p>
  </div>

  <div class="brand"><span class="brand-dot"></span>Harborlane Lending</div>

  <address class="company">
    <span class="name">Harborlane Lending Services, Inc.</span><br>
    7200 Wexmoor Road,<br>
    Brentmoor, MD 21099<br>
    <span class="web">www.harborlanelend.example</span><br>
    NMLS #318674
  </address>
</body>
</html>
```